Hello my name is Colin, I am Starting a business called Harbor Health and fitness and am in need of a memorable business card.
It is a personal training studio. I have added the logo that i would like to be on the left center om my business card. i would like room left up the top for a heading sentence such as. "Is your body shocking for all the wrong reasons". there must be room left on the right of the logo below the main heading for 3 sub headings.
then under those 3 headings and logo room for another larger heading eg. "give me a call and learn how to eat chocolate, drink bear and have great sex". in what room is left i would like to be used for my contact details, use I'm Colin Pettersby your fitness expert on the left then on the right Phone, Email and website space in at least 12 Point. Very specific i know :) now onto the back, for the back i would like an eye catching graphic and room for one main headline and 3 bullet points centered just write anything i will choose what to put in them when i pick a winner. Thank you very much for sticking through all of that :) i appreciate you taking the time to read it and hopefully undergo designing me a business card.
I can't wait to see the designs!

Target Market(s)

slightly more towards females although it would probably be best if it was targeted towards both sexes

Industry/Entity Type

Training

Requirements
Nice to have
• I would love to see if anyone could come up with a design that would really make my card stand out and be memorable.
Should not have
• tacky fitness photos of abs and muscles etc.

```html
<!DOCTYPE html>
<html lang="en">
<head>
<meta charset="utf-8">
<title>Harbor Health and Fitness – Business Card</title>
<link rel="stylesheet" href="https://fonts.googleapis.com/css2?family=Questrial&family=Quicksand:wght@500&family=Michroma&display=swap">
<style>
  :root {
    --stage: #808080;
    --card-black: #070707;
    --electric-blue: #0a14f0;
    --brand-purple: #2a1a8c;
    --name-red: #c4000e;
    --text-white: #ffffff;
    --text-blush: #f3dcef;
    --ink-dark: #0b0b0b;
  }
  * { margin: 0; padding: 0; box-sizing: border-box; }
  html, body {
    width: 1200px; height: 1163px; overflow: hidden;
    background: var(--stage);
  }
  .canvas {
    position: relative; width: 1200px; height: 1163px;
    display: flex; flex-direction: column; align-items: center; justify-content: center; gap: 40px;
  }
  .card {
    position: relative; width: 900px; height: 514px; overflow: hidden;
    background: var(--card-black);
  }
  .card-bands { position: absolute; inset: 0; width: 100%; height: 100%; }
  .band { fill: var(--electric-blue); }

  /* Front */
  .brand-lockup { position: absolute; left: 48px; top: 28px; }
  .brand-name {
    font-family: "Questrial", sans-serif; font-size: 96px; line-height: 1;
    color: var(--brand-purple); letter-spacing: -1px;
  }
  .brand-sub {
    font-family: "Questrial", sans-serif; font-size: 28px; color: var(--ink-dark);
    margin-left: 110px; margin-top: -4px;
  }
  .tagline {
    position: absolute; left: 56px; top: 192px; width: 280px;
    font-family: "Quicksand", sans-serif; font-weight: 500; font-size: 22px; line-height: 1.3;
    color: var(--text-white);
  }
  .promise {
    position: absolute; right: 40px; top: 150px; width: 380px; text-align: right;
    font-family: "Quicksand", sans-serif; font-weight: 500; font-size: 24px; line-height: 1.3;
    color: var(--text-blush);
  }
  .trainer { position: absolute; left: 300px; top: 330px; }
  .trainer-name {
    font-family: "Michroma", sans-serif; font-size: 38px; color: var(--name-red);
  }
  .trainer-role {
    font-family: "Michroma", sans-serif; font-size: 24px; color: var(--text-white);
    margin-left: 40px; margin-top: 2px;
  }

  /* Back */
  .back-heading {
    position: absolute; left: 110px; top: 20px; white-space: nowrap;
    font-family: "Questrial", sans-serif; font-size: 80px; line-height: 1.1; color: var(--ink-dark);
  }
  .back-mark {
    position: absolute; left: 60px; top: 200px; display: flex; align-items: center; gap: 18px;
  }
  .back-mark-circle {
    width: 150px; height: 150px; border-radius: 50%;
    border: 22px solid var(--brand-purple);
  }
  .back-mark-name {
    font-family: "Questrial", sans-serif; font-size: 64px; color: var(--brand-purple);
  }
  .contact-label {
    position: absolute; font-family: "Michroma", sans-serif; font-size: 30px; color: var(--text-blush);
  }
  .contact-email { left: 520px; top: 255px; }
  .contact-phone { left: 50px; top: 430px; }
</style>
</head>
<body>
<main class="canvas">

  <section class="card card-front" aria-label="Business card front">
    <svg class="card-bands" viewBox="0 0 900 514" aria-hidden="true">
      <polygon class="band" points="0,150 360,0 720,0 0,440"/>
      <polygon class="band" points="900,300 900,514 640,514"/>
    </svg>
    <div class="brand-lockup">
      <div class="brand-name">Harbor</div>
      <div class="brand-sub">Health and Fitness</div>
    </div>
    <p class="tagline">"Is your body shocking for all the wrong reasons".</p>
    <p class="promise">"Give me a call and learn how to eat chocolate, drink beer and have great sex"</p>
    <div class="trainer">
      <div class="trainer-name">Colin Pettersby</div>
      <div class="trainer-role">your fitness expert</div>
    </div>
  </section>

  <section class="card card-back" aria-label="Business card back">
    <svg class="card-bands" viewBox="0 0 900 514" aria-hidden="true">
      <polygon class="band" points="0,0 900,0 900,132 0,160"/>
      <polygon class="band" points="0,380 0,514 300,514"/>
    </svg>
    <div class="back-heading">Health and Fitness</div>
    <div class="back-mark">
      <div class="back-mark-circle"></div>
      <div class="back-mark-name">Harbor</div>
    </div>
    <div class="contact-label contact-email">E-mail:</div>
    <div class="contact-label contact-phone">Phone:</div>
  </section>

</main>
</body>
</html>
```